Label for Skincare Brand

"Fernleigh Vale Organics" - organic skincare brand
I need a label designed for my organic skincare brand. I have attached pics of brands I like, to give you an idea of style. I would like something minimal although some colour might work. Colours I like are pale blush pink and aqua. I would like a clean, minimalistic modern yet elegant label. Please look at the samples because they demonstrate the style I look for in a label. It is okay to add a graphical element into the design as long as it enhances or add value to the design.
We do not have a logo yet, so I'd appreciate if you could create a simple type logo for Fernleigh Vale Organics similar to the examples attached.
Please can you do two different sizes: one cream jar and one serum bottle. Both will contain the same information.
___________________________________________________
1. Cream Jar (label size 42 x 190 mm) (clear glass with aluminium lid)
2. Serum Bottle (label size 50 x 110 mm) (clear glass with black pump)
FRONT SIDE:
Fernleigh Vale Organics
Nine Moons
Ultimate Anti-Aging Cream
For Dry & Mature Skin
Organic & Palm Oil-Free
100 ml.
BACK SIDE:
Nine Moons Ultimate Anti-Aging Cream
An effective Day Cream that harnesses the best of science to target the signs of aging. The main active ingredient is R58, a patented noncomedogenic lipid complex, carefully engineered from botanically-sourced lipids. It is composed of a variety of lipid types which are carefully combined in the same ratio as those found on healthy young skin of an average 22 year old.
Directions:
Apply to clean skin morning and night.
Ingredients:
Aloe Vera Leaf Juice, Cocos Nucifera Oil, Butyrospermum Parkii Butter, Jojoba Oil/Macadamia Seed Oil Esters (and) Squalene (and) Phytosteryl Macadamiate (and) Phytosterols, Potassium Olivoyl Hydrolyzed Oat Protein (and) Cetearyl Alcohol (and) Glyceryl Oleate (and) Glyceryl Stearat, Benzyl Alcohol, Dehydroacetic Acid.
Fernleigh Vale Organics
6/3 Kelmora Street North, Bellbrae Heights, NSW 2190
www.fernleighvaleorganics.com.au
Any questions, please just ask away. Thank you.

```html
<!DOCTYPE html>
<html lang="en">
<head>
<meta charset="utf-8">
<title>Fernleigh Vale Organics – Nine Moons Labels</title>
<link rel="stylesheet" href="https://fonts.googleapis.com/css2?family=Arvo:wght@700&family=Open+Sans:wght@300;400;600&display=swap">
<style>
  :root {
    --bg: #efefef;
    --label: #ffffff;
    --ink: #7b7c72;
    --ink-soft: #8e8f86;
    --band: #8a8b81;
    --tab: #d8d8d2;
    --rule: #b9bab2;
  }
  * { box-sizing: border-box; margin: 0; padding: 0; }
  html, body { width: 1200px; height: 1200px; overflow: hidden; background: var(--bg); }
  .canvas {
    position: relative; width: 1200px; height: 1200px; overflow: hidden;
    background: var(--bg); color: var(--ink);
    font-family: "Open Sans", Arial, sans-serif;
  }

  /* brand wordmark */
  .brand-mark {
    position: absolute; top: 120px; right: 90px;
    display: flex; align-items: center; gap: 22px;
  }
  .brand-mark .dot { width: 18px; height: 18px; border-radius: 50%; background: var(--ink); }
  .wordmark {
    font-family: "Open Sans", Arial, sans-serif; font-weight: 300;
    color: var(--ink); text-transform: uppercase; line-height: 1.08;
  }
  .brand-mark .wordmark { font-size: 52px; letter-spacing: 2px; }
  .wordmark span { display: block; letter-spacing: 0.14em; }

  /* shared label parts */
  .label { position: absolute; background: var(--label); box-shadow: 0 1px 3px rgba(0,0,0,0.08); }
  .front { display: flex; flex-direction: column; }
  .front .wordmark { font-size: 19px; letter-spacing: 0.5px; }
  .product-name {
    font-family: "Arvo", Georgia, serif; font-weight: 700; color: var(--ink);
    border-left: 5px solid var(--ink); padding-left: 10px; line-height: 1.1;
  }
  .product-type {
    text-transform: uppercase; color: var(--ink); font-weight: 400;
    border-top: 1.5px solid var(--rule); border-bottom: 1.5px solid var(--rule);
    margin-left: 15px;
  }
  .claims { list-style: none; margin-left: 15px; }
  .claims li { display: flex; align-items: center; gap: 8px; color: var(--ink); }
  .claims svg { flex: none; }
  .volume-band { display: flex; align-items: stretch; background: var(--band); }
  .volume-tab {
    background: var(--tab); color: var(--ink); font-weight: 400;
    display: flex; align-items: center; border-top-right-radius: 22px;
  }

  /* serum bottle label */
  .serum-label { left: 90px; top: 330px; width: 400px; height: 470px; }
  .serum-label .front { height: 100%; padding-top: 40px; }
  .serum-label .inner { padding: 0 30px; }
  .serum-label .product-name { font-size: 54px; margin-top: 30px; }
  .serum-label .product-type { font-size: 18px; padding: 6px 0; margin-top: 6px; }
  .serum-label .claims { margin-top: 16px; }
  .serum-label .claims li { font-size: 17px; margin-bottom: 6px; }
  .serum-label .volume-band { margin-top: auto; margin-bottom: 34px; height: 56px; }
  .serum-label .volume-tab { font-size: 18px; width: 140px; padding-left: 30px; }

  /* cream jar label (wrap) */
  .jar-label {
    left: 80px; top: 875px; width: 1040px; height: 240px;
    display: grid; grid-template-columns: 320px 1fr 320px;
  }
  .back-panel { padding: 22px 24px; font-size: 9.6px; line-height: 1.38; color: var(--ink-soft); }
  .back-panel h3 { font-size: 10.5px; font-weight: 600; color: var(--ink); margin-bottom: 3px; }
  .back-panel h4 { font-size: 9.6px; font-weight: 600; color: var(--ink); margin-top: 7px; }
  .back-panel p { text-align: justify; }
  .jar-label .front { padding-top: 26px; border-left: 1px solid #f0f0ee; border-right: 1px solid #f0f0ee; }
  .jar-label .inner { padding: 0 24px 0 40px; }
  .jar-label .front .wordmark { font-size: 15px; }
  .jar-label .product-name { font-size: 38px; margin-top: 14px; }
  .jar-label .product-type { font-size: 13.5px; padding: 4px 0; margin-top: 4px; }
  .jar-label .claims { margin-top: 8px; }
  .jar-label .claims li { font-size: 13px; margin-bottom: 3px; }
  .jar-label .volume-band { margin-top: auto; margin-bottom: 20px; height: 38px; margin-left: 40px; background: transparent; }
  .jar-label .volume-tab { background: var(--band); color: #f4f4f1; font-size: 14px; width: 110px; padding-left: 16px; }
  .company { margin-top: 7px; color: var(--ink); }
  .company strong { font-weight: 600; }
</style>
</head>
<body>
<main class="canvas">

  <header class="brand-mark">
    <div class="dot"></div>
    <div class="wordmark">Fernleigh Vale<span>Organics</span></div>
  </header>

  <section class="label serum-label" aria-label="Serum bottle label">
    <div class="front">
      <div class="inner">
        <div class="wordmark">Fernleigh Vale<span>Organics</span></div>
        <h1 class="product-name">Nine Moons</h1>
        <p class="product-type">Ultimate Anti-Aging Serum</p>
        <ul class="claims">
          <li><svg width="13" height="13" viewBox="0 0 13 13"><rect x="0.75" y="0.75" width="11.5" height="11.5" fill="none" stroke="currentColor" stroke-width="1.3"/><path d="M3 6.5l2.4 2.4L10.5 3.5" fill="none" stroke="currentColor" stroke-width="1.5"/></svg>For Dry &amp; Mature Skin</li>
          <li><svg width="13" height="13" viewBox="0 0 13 13"><rect x="0.75" y="0.75" width="11.5" height="11.5" fill="none" stroke="currentColor" stroke-width="1.3"/><path d="M3 6.5l2.4 2.4L10.5 3.5" fill="none" stroke="currentColor" stroke-width="1.5"/></svg>Organic &amp; Palm Oil-Free</li>
        </ul>
      </div>
      <div class="volume-band"><div class="volume-tab">100 ml</div></div>
    </div>
  </section>

  <section class="label jar-label" aria-label="Cream jar wrap label">
    <div class="back-panel">
      <h3>Nine Moons Ultimate Anti-Aging Cream</h3>
      <p>An effective Day Cream that harnesses the best of science to target the signs of aging. The main active ingredient is R58, a patented noncomedogenic lipid complex, carefully engineered from botanically-sourced lipids. It is composed of a variety of lipid types which are carefully combined in the same ratio as those found on healthy young skin of an average 22 year old.</p>
      <h4>Directions:</h4>
      <p>Apply to clean skin morning and night.</p>
    </div>

    <div class="front">
      <div class="inner">
        <div class="wordmark">Fernleigh Vale<span>Organics</span></div>
        <h2 class="product-name">Nine Moons</h2>
        <p class="product-type">Ultimate Anti-Aging Serum</p>
        <ul class="claims">
          <li><svg width="11" height="11" viewBox="0 0 13 13"><rect x="0.75" y="0.75" width="11.5" height="11.5" fill="none" stroke="currentColor" stroke-width="1.3"/><path d="M3 6.5l2.4 2.4L10.5 3.5" fill="none" stroke="currentColor" stroke-width="1.5"/></svg>For Dry &amp; Mature Skin</li>
          <li><svg width="11" height="11" viewBox="0 0 13 13"><rect x="0.75" y="0.75" width="11.5" height="11.5" fill="none" stroke="currentColor" stroke-width="1.3"/><path d="M3 6.5l2.4 2.4L10.5 3.5" fill="none" stroke="currentColor" stroke-width="1.5"/></svg>Organic &amp; Palm Oil-Free</li>
        </ul>
      </div>
      <div class="volume-band"><div class="volume-tab">100 ml</div></div>
    </div>

    <div class="back-panel">
      <h4 style="margin-top:0">Ingredients:</h4>
      <p>Aloe Vera Leaf Juice, Cocos Nucifera Oil, Butyrospermum Parkii Butter, Jojoba Oil/Macadamia Seed Oil Esters (and) Squalene (and) Phytosteryl Macadamiate (and) Phytosterols, Potassium Olivoyl Hydrolyzed Oat Protein (and) Cetearyl Alcohol (and) Glyceryl Oleate (and) Glyceryl Stearat, Benzyl Alcohol, Dehydroacetic Acid.</p>
      <p class="company"><strong>Fernleigh Vale Organics</strong><br>6/3 Kelmora Street North, Bellbrae Heights, NSW 2190<br>www.fernleighvaleorganics.com.au</p>
    </div>
  </section>

</main>
</body>
</html>
```